Business Card for my New Brokerage

Looking to get a business card design for my new Real Estate Brokerage.
I want it with Picture, Phone Number, Email, Website, Office Address
Name and Designation. Please add logo too.

Target Market(s)

Real Estate Investors or Home Buyers

Industry/Entity Type

Real Estate

Contact Information for Business Card

Name, Email, Phone Number, website, email, office address

Colors
EB3D1F
EC4F4E
F09395
F8D3D4
FCEDEE

Requirements
Must have
• Minimalistic, Clean, Modern, Photo
Nice to have
• White and Red Colors

```html
<!DOCTYPE html>
<html lang="en">
<head>
<meta charset="UTF-8">
<title>Ember Realty Inc – Business Card</title>
<link rel="stylesheet" href="https://fonts.googleapis.com/css2?family=Montserrat:wght@600;700&family=Questrial&family=Libre+Baskerville&display=swap">
<style>
  :root {
    --red: #e0232b;
    --gold-light: #f8f4c4;
    --gold-mid: #e8cf7a;
    --gold-deep: #c9a44a;
    --paper: #f7f9fb;
    --ghost: #eceef1;
    --ink: #4a4a4a;
    --ink-soft: #7a7a7a;
    --backdrop: #e4e4e6;
  }
  * { box-sizing: border-box; margin: 0; padding: 0; }
  html, body { width: 1200px; height: 800px; overflow: hidden; }
  body {
    background: var(--backdrop);
    position: relative;
    font-family: "Questrial", sans-serif;
  }
  .card {
    position: absolute;
    width: 540px;
    height: 309px;
    background: var(--paper);
    overflow: hidden;
    box-shadow: 0 6px 18px rgba(0,0,0,0.12);
  }
  .card-front { left: 40px; top: 246px; }
  .card-back { left: 620px; top: 246px; }
  .card-art { position: absolute; inset: 0; width: 100%; height: 100%; }

  .brand {
    position: absolute;
    display: flex;
    align-items: center;
    gap: 8px;
    color: var(--red);
    font-family: "Montserrat", sans-serif;
    font-weight: 700;
    letter-spacing: 0.02em;
    white-space: nowrap;
  }
  .brand-mark {
    width: 8px; height: 8px;
    background: var(--red);
  }
  .card-front .brand { left: 250px; top: 96px; font-size: 22px; }
  .address {
    position: absolute;
    left: 250px; top: 146px;
    font-family: "Libre Baskerville", serif;
    font-size: 11.5px;
    color: var(--ink-soft);
    line-height: 1.6;
  }

  .card-back .brand {
    left: 58px; top: 262px;
    font-size: 17px;
    transform: rotate(-90deg);
    transform-origin: 0 0;
  }
  .portrait {
    position: absolute;
    left: 372px; top: 30px;
    width: 120px; height: 110px;
    background: linear-gradient(180deg, #d9c1b0 0%, #c9a995 45%, #2c3448 46%, #222a3c 100%);
  }
  .portrait-band {
    position: absolute;
    left: 440px; top: 132px;
    width: 100px; height: 9px;
    background: var(--red);
  }
  .person {
    position: absolute;
    left: 330px; top: 148px;
  }
  .person-name {
    display: flex;
    align-items: center;
    gap: 6px;
    font-family: "Montserrat", sans-serif;
    font-weight: 700;
    font-size: 20px;
    color: var(--red);
  }
  .person-surname {
    background: var(--red);
    color: #fff;
    font-family: "Questrial", sans-serif;
    font-weight: 400;
    font-size: 12px;
    padding: 3px 8px;
    border-radius: 3px;
  }
  .person-title {
    margin-top: 2px;
    font-size: 13px;
    color: var(--ink);
  }
  .contacts {
    list-style: none;
    margin-top: 8px;
  }
  .contact {
    display: flex;
    align-items: center;
    gap: 8px;
    font-size: 12px;
    color: var(--ink);
    margin-bottom: 4px;
  }
  .contact-icon {
    width: 14px; height: 14px;
    flex: none;
  }
</style>
</head>
<body>

  <section class="card card-front" aria-label="Card front">
    <svg class="card-art" viewBox="0 0 540 309" aria-hidden="true">
      <defs>
        <linearGradient id="gold" x1="0" y1="0" x2="1" y2="1">
          <stop offset="0" stop-color="#e8cf7a"/>
          <stop offset="0.45" stop-color="#f8f4c4"/>
          <stop offset="1" stop-color="#c9a44a"/>
        </linearGradient>
      </defs>
      <rect width="540" height="309" fill="var(--paper)"/>
      <polygon points="0,0 125,0 65,309 0,309" fill="url(#gold)"/>
      <polygon points="125,0 195,0 160,160 540,272 540,309 460,309 175,228 140,309 65,309" fill="var(--red)"/>
      <polygon points="175,228 460,309 140,309" fill="url(#gold)"/>
      <g fill="var(--red)">
        <rect x="200" y="262" width="17" height="17"/>
        <rect x="221" y="262" width="17" height="17"/>
        <rect x="200" y="283" width="17" height="17"/>
        <rect x="221" y="283" width="17" height="17"/>
      </g>
    </svg>
    <div class="brand"><span class="brand-name">EMBER REALTY INC</span><span class="brand-mark"></span></div>
    <p class="address">2150 Harbor Crest Dr. Ashford, CA 94120</p>
  </section>

  <section class="card card-back" aria-label="Card back">
    <svg class="card-art" viewBox="0 0 540 309" aria-hidden="true">
      <rect width="540" height="309" fill="var(--paper)"/>
      <polygon points="200,0 245,0 205,150 175,309 125,309" fill="var(--ghost)"/>
      <polygon points="205,100 540,215 540,262 215,160" fill="var(--ghost)"/>
      <polygon points="210,155 420,309 165,309" fill="var(--red)"/>
      <g fill="#fff">
        <rect x="214" y="252" width="17" height="17"/>
        <rect x="235" y="252" width="17" height="17"/>
        <rect x="214" y="273" width="17" height="17"/>
        <rect x="235" y="273" width="17" height="17"/>
      </g>
    </svg>
    <div class="brand"><span class="brand-name">EMBER REALTY INC</span><span class="brand-mark"></span></div>

    <div class="portrait" role="img" aria-label="Portrait photo of the broker in a dark suit"></div>
    <div class="portrait-band"></div>

    <div class="person">
      <p class="person-name">DANIEL <span class="person-surname">REYES</span></p>
      <p class="person-title">Chief Executive Officer</p>
      <ul class="contacts">
        <li class="contact">
          <svg class="contact-icon" viewBox="0 0 14 14" aria-hidden="true"><circle cx="7" cy="7" r="7" fill="var(--red)"/><path d="M4.5 3.5l1.3 0 .6 1.8-.8.6a4.5 4.5 0 0 0 2.5 2.5l.6-.8 1.8.6v1.3a1 1 0 0 1-1 .8A6 6 0 0 1 3.7 4.5a1 1 0 0 1 .8-1z" fill="#fff"/></svg>
          555-214-0187
        </li>
        <li class="contact">
          <svg class="contact-icon" viewBox="0 0 14 14" aria-hidden="true"><circle cx="7" cy="7" r="7" fill="var(--red)"/><rect x="3.5" y="4.5" width="7" height="5" fill="#fff"/><path d="M3.5 4.5l3.5 2.8 3.5-2.8" fill="none" stroke="var(--red)" stroke-width="0.8"/></svg>
          hello@emberrealty.com
        </li>
        <li class="contact">
          <svg class="contact-icon" viewBox="0 0 14 14" aria-hidden="true"><circle cx="7" cy="7" r="7" fill="var(--red)"/><g fill="none" stroke="#fff" stroke-width="0.8"><circle cx="7" cy="7" r="3.6"/><ellipse cx="7" cy="7" rx="1.5" ry="3.6"/><path d="M3.4 7h7.2"/></g></svg>
          www.emberrealty.com
        </li>
      </ul>
    </div>
  </section>

</body>
</html>
```